Copper Thistle beer can label

Revamping our original 12 oz copper thistle beer can design to look more like our new seasonal can designs....I will supply format, PMS/Color template and brand logo. Must provide multiple formats. .Jpeg, PDF, AI. I am looking for swarming bees around a nest with dripping honey/combs possible blueberrys as well.
Updates

Colors

Designer to choose colors to be used in the design.

Requirements
Must have
• I am looking for a similar layout as my Rusty Anchor Ale label.... Only 2/3 colors with contrasting shading.... Please note the Copper Thistle label predominately must stay within the blue color pallet from original design. No Clip Art!! More silhouette look and feel please.
Nice to have
• Looking to remove wood grain background and add silhouette honey bees swarming around a bees nest...but the bees nest is a spiral sihloette figure. More shading and fades of background.

```html
<!DOCTYPE html>
<html lang="en">
<head>
<meta charset="utf-8">
<title>Copper Thistle – Beer Label</title>
<link href="https://fonts.googleapis.com/css2?family=PT+Sans:ital,wght@0,400;0,700;1,400&family=Alfa+Slab+One&family=IM+Fell+English:ital@1&display=swap" rel="stylesheet">
<style>
  :root {
    --page-bg: #e6e8e9;
    --label-deep: #2a0ea8;
    --label-mid: #3a2cc0;
    --label-soft: #4b48c6;
    --band-lavender: #9ea2dc;
    --title-blue: #3a3fbf;
    --gold: #e2b53c;
    --gold-dark: #b89224;
    --logo-white: #eef0fb;
    --stripe-white: #ffffff;
  }
  * { margin: 0; padding: 0; box-sizing: border-box; }
  html, body {
    width: 1200px;
    height: 977px;
    overflow: hidden;
    background: var(--page-bg);
  }
  .canvas {
    position: relative;
    width: 1200px;
    height: 977px;
  }
  .label {
    position: absolute;
    left: 100px;
    top: 110px;
    width: 1000px;
    height: 760px;
    background: linear-gradient(160deg, var(--label-deep) 0%, var(--label-mid) 55%, var(--label-soft) 100%);
    overflow: hidden;
  }
  .label__notice {
    position: absolute;
    top: 38px;
    left: 0;
    width: 100%;
    text-align: center;
    font-family: "PT Sans", sans-serif;
    font-size: 21px;
    color: var(--gold);
    letter-spacing: 0.3px;
  }
  .label__notice em { font-style: italic; }
  .label__hive {
    position: absolute;
    left: 40px;
    top: 130px;
    width: 400px;
    height: 400px;
    border-radius: 8px;
    background: radial-gradient(ellipse at 55% 45%, rgba(226,181,60,0.55) 0%, rgba(226,181,60,0.25) 55%, rgba(226,181,60,0) 80%);
  }
  .label__brand {
    position: absolute;
    left: 520px;
    top: 300px;
    display: flex;
    align-items: center;
    gap: 18px;
  }
  .label__brand-mark {
    width: 26px;
    height: 26px;
    background: var(--logo-white);
  }
  .label__brand-name {
    font-family: "PT Sans", sans-serif;
    font-weight: 700;
    font-size: 64px;
    color: var(--logo-white);
    letter-spacing: 1px;
  }
  .label__title-band {
    position: absolute;
    left: 0;
    top: 560px;
    width: 100%;
    height: 100px;
    background: var(--band-lavender);
    display: flex;
    align-items: center;
    justify-content: center;
  }
  .label__title {
    font-family: "Alfa Slab One", serif;
    font-size: 76px;
    color: var(--title-blue);
    letter-spacing: 1px;
  }
  .label__stripe {
    position: absolute;
    left: 0;
    top: 682px;
    width: 100%;
    height: 38px;
    background: var(--stripe-white);
    display: flex;
    align-items: center;
    justify-content: center;
  }
  .label__credit {
    font-family: "IM Fell English", serif;
    font-style: italic;
    font-size: 24px;
    color: var(--gold-dark);
  }
</style>
</head>
<body>
<div class="canvas">
  <section class="label">
    <p class="label__notice">Please keep refrigerated at all times…. <em>You don’t want to waste it.</em></p>

    <div class="label__hive" role="img" aria-label="Gold line illustration of a spiral beehive with honey bees swarming around it"></div>

    <div class="label__brand">
      <span class="label__brand-mark"></span>
      <span class="label__brand-name">Ridge &amp; Cask</span>
    </div>

    <div class="label__title-band">
      <h1 class="label__title">Copper Thistle</h1>
    </div>

    <div class="label__stripe">
      <p class="label__credit">Brewed and Canned By:</p>
    </div>
  </section>
</div>
</body>
</html>
```